Cannabis Security Company- Sales Flyer

Take the copy and make a sleek design- no cannabis leave or paraphernalia. Add graphic elements to the Product Offering section

```html
<!DOCTYPE html>
<html lang="en">
<head>
<meta charset="utf-8">
<title>Coreline Security – Sales Flyer</title>
<link rel="stylesheet" href="https://fonts.googleapis.com/css2?family=Montserrat:wght@400;500;600;700;800&display=swap">
<style>
  :root{
    --page-bg:#e9e7e4;
    --paper:#ffffff;
    --ink:#2a2a2a;
    --black:#1d1d1d;
    --grey:#7b7b7b;
    --grey-mid:#8c8c8c;
    --grey-light:#cfcfcf;
    --hero-dark:#1f3436;
    --hero-mid:#4d6a6c;
    --hero-light:#9fb5b6;
    --white:#ffffff;
  }
  *{box-sizing:border-box;margin:0;padding:0}
  html,body{width:1200px;height:1200px;overflow:hidden}
  body{background:var(--page-bg);font-family:'Montserrat',sans-serif;color:var(--ink);position:relative}

  .flyer{position:absolute;left:200px;top:35px;width:800px;height:1130px;background:var(--paper);overflow:hidden;box-shadow:0 6px 24px rgba(0,0,0,.18)}

  .hero{position:absolute;left:0;top:0;width:800px;height:420px;
    background:radial-gradient(ellipse at 72% 40%,var(--hero-light) 0%,var(--hero-mid) 35%,var(--hero-dark) 80%)}
  .brand{position:absolute;left:46px;top:120px;color:var(--white);font-weight:800;font-size:64px;letter-spacing:4px;line-height:1}
  .brand-sub{position:absolute;left:330px;top:92px;color:var(--white);font-weight:600;font-size:15px;letter-spacing:2px}

  .headline-tab{position:absolute;left:0;top:334px;height:44px;padding:0 26px 0 40px;background:var(--grey-mid);color:var(--white);font-weight:700;font-size:25px;line-height:44px}
  .headline-band{position:absolute;left:0;top:378px;width:730px;height:50px;background:var(--black);color:var(--white);font-weight:800;font-size:27px;line-height:50px;padding-left:40px;text-transform:uppercase}

  .body{position:absolute;left:40px;top:446px;width:440px;font-size:12.5px;line-height:1.4}
  .intro{margin-bottom:14px}
  .offer-pill{display:inline-block;background:var(--grey);color:var(--white);font-weight:700;font-size:17px;padding:5px 22px 5px 14px;border-radius:0 16px 16px 0;margin-bottom:10px}
  .checklist{list-style:none}
  .checklist li{position:relative;padding-left:24px;margin-bottom:9px}
  .checklist li svg{position:absolute;left:0;top:3px}
  .bullets{list-style:none;padding-left:24px;margin-bottom:16px}
  .bullets li{position:relative;padding-left:12px;margin-bottom:4px}
  .bullets li::before{content:"";position:absolute;left:0;top:7px;width:5px;height:5px;border-radius:50%;background:var(--ink)}
  .cta{font-weight:700;font-size:15px}

  .products{position:absolute;left:506px;top:448px;width:274px;height:430px;background:var(--grey);border-radius:18px}
  .products-head{position:absolute;left:494px;top:448px;width:286px;height:46px;background:var(--black);color:var(--white);font-weight:700;font-size:17px;line-height:46px;padding-left:18px;letter-spacing:.5px}
  .product{position:absolute;display:flex;align-items:center;gap:16px;color:var(--white);font-weight:600;font-size:15px}
  .product-icon{width:58px;height:58px;border-radius:50%;background:var(--white);border:3px solid var(--grey-light);display:flex;align-items:center;justify-content:center;flex:none}

  .footer-grey{position:absolute;right:0;top:1020px;width:470px;height:54px;background:var(--grey);color:var(--white);font-size:14px;display:flex;align-items:center;justify-content:space-around;padding-left:30px;clip-path:polygon(24px 0,100% 0,100% 100%,0 100%)}
  .footer-grey span{display:flex;align-items:center;gap:8px}
  .footer-black{position:absolute;left:0;top:1074px;width:800px;height:56px;background:var(--black);color:var(--white);font-weight:700;font-size:24px;display:flex;align-items:center;gap:14px;padding-left:40px}
</style>
</head>
<body>
<main class="flyer">
  <section class="hero" role="img" aria-label="Photo of a businessman in a suit touching a glowing digital padlock interface"></section>
  <div class="brand">CORELINE</div>
  <div class="brand-sub">SECURITY</div>

  <div class="headline-tab">Let Coreline Take Care of your</div>
  <h1 class="headline-band">Surveillance &amp; IT Hardware Needs</h1>

  <section class="body">
    <p class="intro">Due to the regulations put forth by the State of California, there is high cost associated with being in compliance to maintain your license and not receive fines as it pertains to security for your facility. In addition, the data intense programs with the seed-to-sale program can be a hindrance to you doing what you do best- running your business!</p>
    <div class="offer-pill">What Coreline Can Offer</div>
    <ul class="checklist">
      <li><svg width="13" height="13" viewBox="0 0 13 13"><rect x="1" y="1" width="11" height="11" fill="none" stroke="#2a2a2a" stroke-width="1.4"/><path d="M3 6.5l2.3 2.3L10 4" fill="none" stroke="#2a2a2a" stroke-width="1.6"/></svg>Experience- we have been in the IT and video surveillance business for over 20 years</li>
      <li><svg width="13" height="13" viewBox="0 0 13 13"><rect x="1" y="1" width="11" height="11" fill="none" stroke="#2a2a2a" stroke-width="1.4"/><path d="M3 6.5l2.3 2.3L10 4" fill="none" stroke="#2a2a2a" stroke-width="1.6"/></svg>Compliance- our attorney helped write Prop 64 and can keep you in compliance with the ever-changing regulations</li>
      <li><svg width="13" height="13" viewBox="0 0 13 13"><rect x="1" y="1" width="11" height="11" fill="none" stroke="#2a2a2a" stroke-width="1.4"/><path d="M3 6.5l2.3 2.3L10 4" fill="none" stroke="#2a2a2a" stroke-width="1.6"/></svg>Cost Savings- Coreline can save you 15-30% over the competition</li>
      <li><svg width="13" height="13" viewBox="0 0 13 13"><rect x="1" y="1" width="11" height="11" fill="none" stroke="#2a2a2a" stroke-width="1.4"/><path d="M3 6.5l2.3 2.3L10 4" fill="none" stroke="#2a2a2a" stroke-width="1.6"/></svg>Speed- our solutions can be designed and implemented within days, not months</li>
      <li><svg width="13" height="13" viewBox="0 0 13 13"><rect x="1" y="1" width="11" height="11" fill="none" stroke="#2a2a2a" stroke-width="1.4"/><path d="M3 6.5l2.3 2.3L10 4" fill="none" stroke="#2a2a2a" stroke-width="1.6"/></svg>Customization- our products are architected around the business not the business around the products</li>
      <li><svg width="13" height="13" viewBox="0 0 13 13"><rect x="1" y="1" width="11" height="11" fill="none" stroke="#2a2a2a" stroke-width="1.4"/><path d="M3 6.5l2.3 2.3L10 4" fill="none" stroke="#2a2a2a" stroke-width="1.6"/></svg>Finance options- Coreline offers the following options for purchase</li>
    </ul>
    <ul class="bullets">
      <li>Outright purchase- own your own equipment and data</li>
      <li>Leasing with a monthly payment- prevent large outlay of cash</li>
      <li>Managed/cloud offering- we send the gear and manage in a secure location</li>
    </ul>
    <p class="cta">Call us today for a free consultation</p>
  </section>

  <aside class="products" aria-label="Product offering"></aside>
  <h2 class="products-head">PRODUCT OFFERING</h2>

  <div class="product" style="left:480px;top:512px">
    <span class="product-icon"><svg width="30" height="30" viewBox="0 0 30 30"><rect x="5" y="8" width="17" height="9" rx="2" fill="#1d1d1d" transform="rotate(-15 13 12)"/><circle cx="8" cy="13" r="2" fill="#fff"/><path d="M16 17v5h-6M6 19v6" stroke="#1d1d1d" stroke-width="2.5" fill="none"/></svg></span>Video Surveillance</div>
  <div class="product" style="left:494px;top:588px">
    <span class="product-icon"><svg width="30" height="30" viewBox="0 0 30 30" fill="none" stroke="#1d1d1d" stroke-width="2"><ellipse cx="15" cy="7" rx="9" ry="3.5"/><path d="M6 7v16c0 2 4 3.5 9 3.5s9-1.5 9-3.5V7M6 12.5c0 2 4 3.5 9 3.5s9-1.5 9-3.5M6 18c0 2 4 3.5 9 3.5s9-1.5 9-3.5"/></svg></span>Data Storage</div>
  <div class="product" style="left:508px;top:664px">
    <span class="product-icon"><svg width="30" height="30" viewBox="0 0 30 30"><path d="M15 3l10 4v7c0 7-5 11-10 13C10 25 5 21 5 14V7z" fill="#1d1d1d"/><path d="M10 15l3.5 3.5L20 11" stroke="#fff" stroke-width="2.5" fill="none"/></svg></span>Data Security</div>
  <div class="product" style="left:522px;top:740px">
    <span class="product-icon"><svg width="30" height="30" viewBox="0 0 30 30" fill="none" stroke="#1d1d1d" stroke-width="2"><rect x="11" y="3" width="8" height="6"/><rect x="3" y="21" width="8" height="6"/><rect x="19" y="21" width="8" height="6"/><path d="M15 9v6M7 21v-6h16v6"/></svg></span>Networking</div>
  <div class="product" style="left:536px;top:816px">
    <span class="product-icon"><svg width="30" height="30" viewBox="0 0 30 30" fill="none" stroke="#1d1d1d" stroke-width="2"><circle cx="15" cy="15" r="2.5" fill="#1d1d1d"/><path d="M10 10a7 7 0 000 10M20 10a7 7 0 010 10M6.5 6.5a12 12 0 000 17M23.5 6.5a12 12 0 010 17M15 17v10"/></svg></span>Wireless Connectivity</div>

  <div class="footer-grey">
    <span><svg width="18" height="13" viewBox="0 0 18 13" fill="none" stroke="#fff" stroke-width="1.5"><rect x="1" y="1" width="16" height="11"/><path d="M1 1l8 6 8-6"/></svg>info@corelinedistributing.com</span>
    <span><svg width="16" height="16" viewBox="0 0 16 16" fill="none" stroke="#fff" stroke-width="1.3"><circle cx="8" cy="8" r="7"/><path d="M1 8h14M8 1c3 3 3 11 0 14M8 1c-3 3-3 11 0 14"/></svg>www.vaultboxstore.com</span>
  </div>
  <div class="footer-black">
    <svg width="24" height="24" viewBox="0 0 24 24"><path d="M6 3l4 4-2 3c1.5 3 3 4.5 6 6l3-2 4 4-3 3C10 21 3 14 3 6z" fill="#fff"/></svg>
    (555) 014-2290
  </div>
</main>
</body>
</html>
```